Restoration Specialist in need of business card designs

One side of the business card is a bathroom ripped out down to the studs with just a sink and toilet and then the other side is the bathroom (same sink and toilet) but put back together. Like a before and after on each side behind our information. Stand out, hard to forget, business cards for my restoration company. I want a unique concept all together.
Must include in no particular order:
our business name "Summit Renewals"
Possible Logo for a restoration company
Owner; Dennis Moravec
410-386-7294
dmoravec@summitrenewalsqx.example
SummitRenewalsQX.example (our company website) BUT I am open to any and all designs and options.

Target Market(s)

Customers, Men in the mitigation, plumbing, electrical, HVAC, Roofing, insurance companies

Industry/Entity Type

Restoration/ construction

Contact Information for Business Card

Must include in no particular order: our business name "Summit Renewals" Owner; Dennis Moravec 410-386-7294 dmoravec@summitrenewalsqx.example SummitRenewalsQX.example (our company website) MAY include a list of our services: Residential~ Emergency Response ~ Board- up~ Complete Restoration

Font styles to use
Serif

Colors
0054AA
0677BA
7BADD7
CADEEF
E8F1F8
F0912C
F2A743
F7CA91
FBE8D2
FDF5EE

Requirements
Must have
• unique, memorable, not something men have seen over and over again,
Nice to have
• eye catching
Should not have
• Been something I could have made by myself

```html
<!DOCTYPE html>
<html lang="en">
<head>
<meta charset="utf-8">
<title>Summit Renewals – Business Card</title>
<link href="https://fonts.googleapis.com/css2?family=Domine:wght@700&family=Roboto:wght@400;500&display=swap" rel="stylesheet">
<style>
  :root {
    --navy: #12354f;
    --orange: #ec7220;
    --white: #ffffff;
    --backdrop: #c4c4c4;
    --serif: "Domine", Georgia, serif;
    --sans: "Roboto", Arial, sans-serif;
  }
  * { box-sizing: border-box; margin: 0; padding: 0; }
  html, body { width: 1200px; height: 1015px; overflow: hidden; }
  body {
    background: var(--backdrop);
    position: relative;
    font-family: var(--sans);
  }
  .card {
    position: absolute;
    left: 250px;
    width: 700px;
    height: 400px;
    overflow: hidden;
    box-shadow: 0 4px 14px rgba(0,0,0,.25);
  }

  /* Front */
  .card-front { top: 90px; background: var(--navy); }
  .front-brand {
    position: absolute;
    top: 105px;
    left: 0; right: 0;
    text-align: center;
    font-family: var(--serif);
    font-weight: 700;
    font-size: 46px;
    letter-spacing: 1px;
    text-transform: uppercase;
    color: var(--orange);
  }
  .front-rule {
    position: absolute;
    top: 180px;
    left: 205px;
    width: 290px;
    height: 3px;
    background: var(--white);
  }
  .service-band {
    position: absolute;
    top: 262px;
    left: 0;
    width: 100%;
    height: 92px;
    background: var(--orange);
    color: var(--white);
    font-size: 19px;
    font-weight: 500;
    text-align: center;
    display: flex;
    flex-direction: column;
    justify-content: center;
    gap: 4px;
  }
  .bullet {
    display: inline-block;
    width: 7px; height: 7px;
    background: var(--white);
    margin: 0 8px;
    vertical-align: middle;
  }

  /* Back */
  .card-back { top: 525px; background: var(--white); }
  .holder {
    position: absolute;
    top: 48px;
    left: 48px;
  }
  .holder-name {
    font-family: var(--serif);
    font-weight: 700;
    font-size: 30px;
    text-transform: uppercase;
    color: var(--orange);
    line-height: 1;
  }
  .holder-role {
    font-size: 22px;
    color: var(--navy);
    margin-top: 8px;
    padding-bottom: 10px;
    border-bottom: 2px solid var(--navy);
    width: 300px;
  }
  .contact-list {
    list-style: none;
    margin-top: 14px;
    margin-left: 22px;
  }
  .contact-list li {
    display: flex;
    align-items: center;
    gap: 10px;
    font-size: 22px;
    color: var(--navy);
    line-height: 1.3;
  }
  .contact-list svg { width: 20px; height: 20px; flex: none; }
  .back-brand {
    position: absolute;
    left: 110px;
    bottom: 48px;
    font-family: var(--serif);
    font-weight: 700;
    font-size: 42px;
    text-transform: uppercase;
    color: var(--orange);
  }
  .back-rule {
    position: absolute;
    left: 110px;
    bottom: 42px;
    width: 420px;
    height: 3px;
    background: var(--navy);
  }
</style>
</head>
<body>

  <section class="card card-front">
    <div class="front-brand">Summit Renewals</div>
    <div class="front-rule"></div>
    <div class="service-band">
      <p>Residential<span class="bullet"></span>Emergency Response<span class="bullet"></span>Board- up</p>
      <p>Storm Protection<span class="bullet"></span>Complete Restoration</p>
    </div>
  </section>

  <section class="card card-back">
    <div class="holder">
      <h1 class="holder-name">Dennis Moravec</h1>
      <p class="holder-role">Owner</p>
      <ul class="contact-list">
        <li>
          <svg viewBox="0 0 24 24" aria-hidden="true"><path fill="#ec7220" d="M6.6 10.8a15.1 15.1 0 0 0 6.6 6.6l2.2-2.2c.3-.3.7-.4 1-.2 1.1.4 2.3.6 3.6.6.6 0 1 .4 1 1V20c0 .6-.4 1-1 1A17 17 0 0 1 3 4c0-.6.4-1 1-1h3.5c.6 0 1 .4 1 1 0 1.3.2 2.5.6 3.6.1.3 0 .7-.2 1z"/></svg>
          410-386-7294
        </li>
        <li>
          <svg viewBox="0 0 24 24" aria-hidden="true"><path fill="#ec7220" d="M2 5h20v14H2z"/><path fill="none" stroke="#fff" stroke-width="1.6" d="M2 5l10 8 10-8"/></svg>
          dmoravec@summitrenewalsqx.example
        </li>
        <li>
          <svg viewBox="0 0 24 24" aria-hidden="true"><circle cx="12" cy="12" r="10" fill="#ec7220"/><path fill="none" stroke="#fff" stroke-width="1.3" d="M2 12h20M12 2v20M12 2c-4 4-4 16 0 20M12 2c4 4 4 16 0 20"/></svg>
          SummitRenewalsQX.example
        </li>
      </ul>
    </div>
    <div class="back-brand">Summit Renewals</div>
    <div class="back-rule"></div>
  </section>

</body>
</html>
```